Stationary for Keeping Steady

we are in the process of creating a more professional image for our company Keeping Steady Paramedical Services. We have recently had a new logo and general brochure designed using artpitchhub and have been impressed by the quality of submissions.

We need:
- Letterhead (A4)
- Business Cards
- With compliments slips
- Email stationary

Letterhead information:
Address - 47 Wattlebrook Drive, Fernhollow Vic 3091
Phone - 1800 462 817
email - enquiries@keepsteady.com.au
Internet - www.keepsteady.com.au
ABN - 82 463 915 207
ACN - 264 871 035

Files need to be able to be edited in Illustrator CS2

Business Cards / with compliments slips / email stationary:
Double sided.
One side to have Name, Mobile number, company phone 1800462817, email, internet address

Files need to be able to be edited in Illustrator CS2 (except email stationary)

Our website is www.keepsteady.com.au for more information. Do not base designs on the website as it will eventually be revised.

Target Market(s)

Australian based businesses, government departments and schools. We specialise in corporate customers rather than public first aid course

Industry/Entity Type

Internet

Requirements
Must have
• Where applicable file to be editable in illustrator CS2 to allow future alterations.

```html
<!DOCTYPE html>
<html lang="en">
<head>
<meta charset="utf-8">
<title>Keeping Steady – Letterhead</title>
<link rel="stylesheet" href="https://fonts.googleapis.com/css2?family=Arimo:wght@400;700&display=swap">
<style>
  :root {
    --frame-outer: #07a4b4;
    --frame-inner: #4ec2d0;
    --frame-edge: #e9f4f6;
    --paper: #f4f5f7;
    --band: #d4eefa;
    --brand-red: #d6303c;
    --contact-teal: #16808c;
  }
  html, body {
    margin: 0;
    padding: 0;
    overflow: hidden;
    background: #ffffff;
  }
  .letterhead {
    position: relative;
    width: 900px;
    height: 1200px;
    background: var(--frame-outer);
    font-family: "Arimo", Arial, sans-serif;
    overflow: hidden;
  }
  .frame-inner {
    position: absolute;
    left: 10px; top: 10px; right: 10px; bottom: 10px;
    background: var(--frame-inner);
  }
  .frame-edge {
    position: absolute;
    left: 20px; top: 20px; right: 12px; bottom: 26px;
    background: var(--frame-edge);
  }
  .paper {
    position: absolute;
    left: 24px; top: 24px; right: 14px; bottom: 28px;
    background: var(--paper);
  }
  .header-band {
    position: absolute;
    left: 28px; top: 30px;
    width: 854px; height: 21px;
    background: var(--band);
  }
  .brand {
    position: absolute;
    left: 130px; top: 84px;
    display: flex;
    align-items: center;
    gap: 18px;
    color: var(--brand-red);
    font-weight: 700;
  }
  .brand-mark {
    width: 90px; height: 90px;
    background: var(--brand-red);
  }
  .brand-name {
    line-height: 1.15;
  }
  .brand-name .line-main { display: block; font-size: 44px; }
  .brand-name .line-sub { display: block; font-size: 21px; }
  .footer-band {
    position: absolute;
    left: 30px; top: 1077px;
    width: 848px; height: 88px;
    background: var(--band);
    color: var(--contact-teal);
    font-size: 13px;
    line-height: 15.2px;
  }
  .address {
    position: absolute;
    left: 18px; top: 6px;
  }
  .registration {
    position: absolute;
    left: 618px; top: 15px;
  }
  .address p, .registration p { margin: 0; }
</style>
</head>
<body>
<div class="letterhead">
  <div class="frame-inner"></div>
  <div class="frame-edge"></div>
  <div class="paper"></div>
  <div class="header-band"></div>

  <div class="brand">
    <div class="brand-mark"></div>
    <div class="brand-name">
      <span class="line-main">Keeping Steady</span>
      <span class="line-sub">Paramedical Services Pty Ltd</span>
    </div>
  </div>

  <footer class="footer-band">
    <div class="address">
      <p>Keeping Steady</p>
      <p>Paramedical services Pty Ltd</p>
      <p>47 Wattlebrook Drive</p>
      <p>Fernhollow Vic 3091</p>
      <p>Phone - 1800 462 817</p>
    </div>
    <div class="registration">
      <p>Email - enquiries@keepsteady.com.au</p>
      <p>Internet - www.keepsteady.com.au</p>
      <p>ABN - 82 463 915 207</p>
      <p>ACN - 264 871 035</p>
    </div>
  </footer>
</div>
</body>
</html>
```